Santa Letter 1

This will be a letter from Santa to a child. Themes on the stationary should be Christmas themed. Religious is ok, but want some that aren't. North pole, Santa, Mrs. Clause, Sleigh, Ornaments, etc. We will pick more than 1 winner because we would like 2-3 designs in the end, all being different. High professional quality is very important.

Target Market(s)

Children and parents of young children

Industry/Entity Type

Religious

Font styles to use
Decorative

Requirements
Must have
• Christmas and holiday themes. The page should have space for text to be printed and easily read. So the design should be near the bottom and on one side more than the other so the text can be printed and easily read.

```html
<!DOCTYPE html>
<html lang="en">
<head>
<meta charset="utf-8">
<title>Santa Letter</title>
<link rel="stylesheet" href="https://fonts.googleapis.com/css2?family=Great+Vibes&family=Yellowtail&display=swap">
<style>
  :root {
    --backdrop: #b9c6c8;
    --page: #ffffff;
    --frost: #d8e6ee;
    --frost-light: #eef4f8;
    --stamp-top: #fafafa;
    --stamp-mid: #ececec;
    --stamp-edge: #1f2a30;
    --ink: #1c1c1c;
    --santa-red: #b3121a;
    --greeting-blue: #1f6fae;
    --greeting-deep: #0f3f6b;
    --art-red: #e7b7b3;
    --art-grey: #e4e4e4;
  }
  * { box-sizing: border-box; margin: 0; padding: 0; }
  html, body {
    width: 1200px; height: 784px; overflow: hidden;
    background: var(--backdrop);
  }
  .letter {
    position: absolute; left: 318px; top: 20px;
    width: 564px; height: 744px;
    background: var(--page);
    padding: 14px;
    box-shadow: 0 4px 14px rgba(40, 60, 70, 0.25);
  }
  .frost-band {
    position: relative; width: 100%; height: 100%;
    background:
      radial-gradient(circle at 12% 70%, rgba(255,255,255,.6) 0 18px, transparent 19px),
      radial-gradient(circle at 8% 82%, rgba(255,255,255,.5) 0 10px, transparent 11px),
      radial-gradient(circle at 90% 20%, rgba(255,255,255,.5) 0 14px, transparent 15px),
      linear-gradient(160deg, var(--frost-light), var(--frost) 60%, var(--frost-light));
  }
  .stamp {
    position: absolute; left: 30px; right: 34px; top: 64px; bottom: 58px;
    background: radial-gradient(ellipse at 70% 25%, var(--stamp-top), var(--stamp-mid) 80%);
    border: 1.5px dashed var(--stamp-edge);
    box-shadow: 6px 8px 0 rgba(150,165,172,.45);
  }
  .stamp::before, .stamp::after {
    content: ""; position: absolute; left: -8px; right: -8px; height: 14px;
    background: radial-gradient(circle at 50% 50%, var(--frost) 5px, transparent 5.6px) repeat-x 0 0 / 16px 14px;
  }
  .stamp::before { top: -8px; }
  .stamp::after { bottom: -8px; }
  .stamp-side {
    position: absolute; top: -8px; bottom: -8px; width: 14px;
    background: radial-gradient(circle at 50% 50%, var(--frost) 5px, transparent 5.6px) repeat-y 0 0 / 14px 16px;
  }
  .stamp-side.left { left: -8px; }
  .stamp-side.right { right: -8px; }
  .holiday-art {
    position: absolute; left: 150px; top: 170px; width: 210px; height: 250px;
    border-radius: 48% 52% 44% 56%;
    background: radial-gradient(ellipse at 50% 45%, var(--art-red), var(--art-grey) 70%, transparent 72%);
    opacity: .55;
  }
  .sender {
    position: absolute; right: 26px; top: 22px;
    font-family: "Yellowtail", "Great Vibes", cursive;
    font-weight: 400; font-size: 64px; line-height: 1.1;
    color: var(--santa-red);
    text-shadow: 2px 2px 0 #fff, 4px 4px 3px rgba(0,0,0,.25);
  }
  .message {
    position: absolute; left: 36px; right: 30px; top: 112px;
    font-family: "Great Vibes", cursive; font-size: 27px; line-height: 41px;
    color: var(--ink);
  }
  .greeting {
    position: absolute; left: 40px; bottom: 52px;
    font-family: "Yellowtail", "Great Vibes", cursive;
    font-weight: 400; font-size: 58px; line-height: 1.1;
    color: var(--greeting-blue);
    text-shadow: 1px 1px 0 var(--greeting-deep), 3px 3px 3px rgba(0,0,0,.2);
  }
</style>
</head>
<body>
  <main class="letter">
    <div class="frost-band">
      <section class="stamp">
        <span class="stamp-side left"></span>
        <span class="stamp-side right"></span>
        <div class="holiday-art" role="img" aria-label="Faint festive holiday artwork in soft red and grey tones"></div>
        <h1 class="sender">Santa</h1>
        <p class="message">Peace and good will to you and your loved ones this Christmas season. Peace and good will to you and your loved ones this Christmas season. Peace and good will to you and your loved ones this Christmas season. Peace and good will to you and your loved ones this Christmas season.</p>
        <p class="greeting">Merry Christmas</p>
      </section>
    </div>
  </main>
</body>
</html>
```